Gutschein-Design Falter Webshop
Zielgruppe
Webshop von Pyrotechnischen Artikeln. Rauchkörper, Bengalische Lichter, Kinderfeuerwerk, klassisches Silvesterfeuerwerk. Der Shop ist zu finden unter https://www.funkenkiste-beispiel.de
Das Format sollte sich an DIN Lang orientieren.
Wenn Artikelbilder oder sonstige Fotos aus dem Shop benötigt werden, können diese gerne angefragt werden.
Aufgabenstellung
Der Shop sollte im Flyer wieder erkennbar sein und nach Möglichkeit alle 5 Hauptkategorien abbilden.
Wobei Silvesterfeuerwerk, Zubehör und Partyartikel die kleinere Rolle spielen.
Rauch und Bengal stehen dabei im Vordergrund
Ein Textfeld sollte enthalten sein, worein wir dann den Gutscheincode / Wert drucken.
Edit: Sorry, ich hatte anfangs die falschen Grafiken hochgeladen. Jetzt ist das Shoplogo in den Files zu finden. Ebenso ein Beispielfoto mit Rauch

```html
<!DOCTYPE html>
<html lang="de">
<head>
<meta charset="utf-8">
<title>Gutschein – Falter Webshop</title>
<link href="https://fonts.googleapis.com/css2?family=Audiowide&display=swap" rel="stylesheet">
<style>
  :root {
    --canvas-bg: #e3e4e4;
    --frame-dark: #2a2a2b;
    --frame-light: #5c5c5e;
    --band-dark: rgba(38,38,40,0.94);
    --label-bg: #3b3b3d;
    --gold: #c59a55;
    --white: #ffffff;
    --foliage-dark: #10260b;
    --foliage-mid: #2c5a1c;
    --foliage-light: #4f7f2c;
    --smoke-white: rgba(238,236,222,0.97);
    --smoke-teal: rgba(44,160,132,0.97);
    --spark-dark: #140d08;
    --spark-amber: rgba(232,150,50,0.9);
    --spark-gold: rgba(255,196,100,0.85);
  }
  * { margin: 0; padding: 0; box-sizing: border-box; }
  html, body { width: 1200px; height: 1200px; overflow: hidden; background: var(--canvas-bg); }
  body { position: relative; font-family: "Audiowide", sans-serif; }

  .voucher {
    position: absolute; left: 100px; width: 988px;
    background: linear-gradient(90deg, var(--frame-dark), var(--frame-light) 50%, var(--frame-dark));
  }
  .voucher--front { top: 85px; height: 503px; }
  .voucher--back  { top: 602px; height: 500px; }

  .voucher__photo { position: absolute; left: 22px; right: 22px; overflow: hidden; }
  .voucher--front .voucher__photo { top: 24px; height: 454px; }
  .voucher--back  .voucher__photo { top: 23px; height: 452px; }

  .photo-fill { position: absolute; inset: 0; }
  .photo-fill--smoke {
    background:
      /* white smoke plume, top left down to the left hand */
      radial-gradient(ellipse 90px 70px at 40px 30px, var(--smoke-white), transparent 75%),
      radial-gradient(ellipse 80px 60px at 95px 80px, var(--smoke-white), transparent 75%),
      radial-gradient(ellipse 70px 55px at 145px 130px, var(--smoke-white), transparent 75%),
      radial-gradient(ellipse 50px 55px at 185px 185px, var(--smoke-white), transparent 75%),
      radial-gradient(ellipse 30px 45px at 210px 235px, var(--smoke-white), transparent 75%),
      /* teal smoke plume, top centre down to the right hand */
      radial-gradient(ellipse 140px 70px at 520px 20px, var(--smoke-teal), transparent 75%),
      radial-gradient(ellipse 110px 70px at 600px 70px, var(--smoke-teal), transparent 75%),
      radial-gradient(ellipse 70px 70px at 650px 140px, var(--smoke-teal), transparent 75%),
      radial-gradient(ellipse 40px 60px at 675px 210px, var(--smoke-teal), transparent 75%),
      /* teal haze lower left */
      radial-gradient(ellipse 80px 110px at 0px 330px, rgba(44,160,132,0.45), transparent 75%),
      /* dark figure area below the band */
      radial-gradient(ellipse 120px 90px at 480px 440px, rgba(20,20,20,0.85), transparent 75%),
      /* foliage tones */
      radial-gradient(ellipse 200px 120px at 330px 120px, var(--foliage-light), transparent 75%),
      radial-gradient(ellipse 220px 140px at 780px 380px, var(--foliage-light), transparent 75%),
      radial-gradient(ellipse 70% 80% at 50% 55%, var(--foliage-mid), var(--foliage-dark));
  }
  .photo-fill--sparks {
    background:
      radial-gradient(ellipse 90px 70px at 415px 185px, var(--spark-gold), transparent 75%),
      radial-gradient(ellipse 260px 160px at 430px 200px, var(--spark-amber), transparent 75%),
      radial-gradient(ellipse 200px 120px at 580px 330px, rgba(232,150,50,0.6), transparent 75%),
      radial-gradient(ellipse 140px 80px at 130px 30px, rgba(232,150,50,0.55), transparent 75%),
      radial-gradient(ellipse 120px 80px at 820px 80px, rgba(232,150,50,0.5), transparent 75%),
      radial-gradient(ellipse 160px 80px at 120px 260px, rgba(232,150,50,0.4), transparent 75%),
      var(--spark-dark);
  }

  .title-band {
    position: absolute; left: 0; right: 0; top: 169px; height: 95px;
    background: linear-gradient(90deg, var(--band-dark), rgba(72,72,74,0.94) 50%, var(--band-dark));
  }
  .title-band__label {
    position: absolute; left: 213px; width: 465px; top: 0; bottom: 0;
    background: var(--label-bg);
    display: flex; align-items: center; justify-content: center;
    color: var(--white); font-size: 63px; letter-spacing: 1px;
  }

  .brand-name {
    position: absolute; right: 52px; top: 362px;
    color: var(--gold); font-size: 32px;
  }

  .categories {
    position: absolute; left: 32px; width: 380px; top: 117px;
    list-style: none; text-align: center;
    color: var(--white); font-size: 30px; line-height: 36px; letter-spacing: 1px;
  }
  .code-field {
    position: absolute; left: 347px; top: 112px; width: 579px; height: 229px;
    background: var(--white); border-radius: 12px;
  }
  .shop-url {
    position: absolute; left: 22px; top: 421px;
    color: var(--white); font-size: 16px; letter-spacing: 0.5px;
  }
  .stars { position: absolute; inset: 0; width: 100%; height: 100%; pointer-events: none; }
  .star--gold { fill: var(--gold); }
  .star--white { fill: var(--white); }
</style>
</head>
<body>

<section class="voucher voucher--front">
  <div class="voucher__photo">
    <div class="photo-fill photo-fill--smoke" role="img" aria-label="Foto: Mann hält zwei brennende Rauchfackeln mit weißem und türkisem Rauch vor grünen Bäumen"></div>
    <div class="title-band"><div class="title-band__label">gutschein</div></div>
    <svg class="stars" viewBox="0 0 944 454" aria-hidden="true">
      <polygon class="star--gold" points="800,20 810,55 845,60 815,75 820,110 800,90 730,130 790,75 770,50 795,55"/>
      <polygon class="star--white" points="900,50 905,68 920,72 905,78 880,110 895,78 885,65 897,65"/>
      <polygon class="star--white" points="838,85 842,97 853,98 843,104 845,116 837,108 826,113 831,103 824,95 836,96"/>
      <polygon class="star--gold" points="150,345 175,355 195,330 190,358 215,372 188,375 180,402 170,378 140,380 160,362"/>
      <polygon class="star--white" points="30,345 42,352 55,340 52,356 62,364 48,364 44,378 38,364 22,362 36,354"/>
      <polygon class="star--white" points="80,335 90,340 100,330 98,343 106,350 95,350 92,360 87,350 75,348 86,343"/>
    </svg>
    <div class="brand-name">funkenkiste</div>
  </div>
</section>

<section class="voucher voucher--back">
  <div class="voucher__photo">
    <div class="photo-fill photo-fill--sparks" role="img" aria-label="Foto: sprühende goldene Funken einer Wunderkerze vor dunklem Hintergrund"></div>
    <svg class="stars" viewBox="0 0 944 452" aria-hidden="true">
      <polygon class="star--gold" points="270,35 290,70 330,75 300,95 340,130 290,105 265,135 260,100 225,90 258,78"/>
      <polygon class="star--gold" points="405,90 415,110 440,112 420,122 440,150 410,130 395,145 395,125 378,115 398,110"/>
      <polygon class="star--gold" points="690,10 698,28 715,30 700,40 705,58 690,45 670,58 680,40 668,28 685,28"/>
      <polygon class="star--gold" points="650,55 660,75 680,78 662,88 668,110 650,95 632,108 640,88 625,78 645,75"/>
      <polygon class="star--white" points="830,10 836,22 848,22 838,30 842,42 830,34 815,42 822,30 814,22 826,22"/>
      <polygon class="star--white" points="100,50 115,70 138,70 120,82 160,112 110,90 95,108 98,85 80,75 102,72"/>
      <polygon class="star--gold" points="780,335 790,360 825,365 795,380 800,415 780,395 755,410 765,380 710,345 770,355"/>
      <polygon class="star--gold" points="730,320 738,335 755,338 740,346 744,362 730,352 715,360 720,345 700,330 725,333"/>
      <polygon class="star--gold" points="310,300 318,316 335,320 320,328 323,345 310,335 295,342 300,327 288,318 305,316"/>
      <polygon class="star--gold" points="330,250 340,265 370,245 348,275 360,290 340,285 325,300 326,282 310,275 328,268"/>
      <polygon class="star--gold" points="140,300 148,315 165,318 150,325 152,340 140,330 125,338 130,323 118,315 135,315"/>
      <polygon class="star--gold" points="170,350 176,360 188,362 178,368 180,380 170,372 158,378 162,366 152,360 166,360"/>
      <polygon class="star--white" points="110,360 116,370 128,370 118,377 120,390 110,382 95,386 103,375 92,368 106,368"/>
      <polygon class="star--white" points="835,400 842,414 858,416 845,425 850,440 835,432 820,440 825,425 812,416 828,414"/>
    </svg>
    <ul class="categories">
      <li>Bengal</li>
      <li>Rauchkörper</li>
      <li>Partyartikel</li>
      <li>Feuerwerk</li>
      <li>Zubehör</li>
    </ul>
    <div class="code-field" aria-label="Feld für Gutscheincode und Wert"></div>
    <div class="shop-url">www.funkenkiste-beispiel.de</div>
  </div>
</section>

</body>
</html>
```